Essential oil label for bottles

Looking to modify our current logo and label design. It looks too simple. I will attach images of our competitors to use as examples. Our company name is Velnora. We have 2 different bottles. Clear and amber color. Going forward, we will be using only the amber bottle. The other 2 images are the biggest sellers brands. We want to make some adjustments to ours.

Target Market(s)

Brindex sales

Industry/Entity Type

Essential oil, perfume

Colors

Designer to choose only greyscale colors for use in the design.

Requirements
Nice to have
• A slight change to fonts and logo design. Maybe change the font and design of the word "Velnora" in our logo. Maybe add something to the label to make it stand out more but still keeping it clean and modern
Should not have
• No colors, besides, black, grays, whites, and off white.

```html
<!DOCTYPE html>
<html lang="en">
<head>
<meta charset="UTF-8">
<title>Velnora — True Path Fragrance Oil Label</title>
<link rel="stylesheet" href="https://fonts.googleapis.com/css2?family=Montserrat:wght@400;500&family=Great+Vibes&display=swap">
<style>
  :root {
    --page-bg: #e4e3df;
    --label-black: #131313;
    --label-ink: #e9e5da;
    --label-rule: #cfcbc1;
  }
  * { margin: 0; padding: 0; box-sizing: border-box; }
  html, body {
    width: 1109px;
    height: 1200px;
    overflow: hidden;
    background: var(--page-bg);
  }
  .canvas {
    position: relative;
    width: 1109px;
    height: 1200px;
  }
  .label {
    position: absolute;
    left: 224px;
    top: 167px;
    width: 660px;
    height: 866px;
    background: var(--label-black);
    color: var(--label-ink);
    font-family: "Montserrat", sans-serif;
  }
  .notes-rule {
    position: absolute;
    left: 135px;
    top: 0;
    width: 2px;
    height: 100%;
    background: var(--label-rule);
  }
  .scent-notes {
    position: absolute;
    left: 92px;
    top: 126px;
    height: 614px;
    writing-mode: vertical-rl;
    transform: rotate(180deg);
    font-size: 23px;
    font-weight: 500;
    letter-spacing: 3.2px;
    text-align: center;
    white-space: nowrap;
  }
  .label-body {
    position: absolute;
    left: 137px;
    right: 0;
    top: 0;
    bottom: 0;
    text-align: center;
  }
  .brand-name {
    position: absolute;
    left: 0;
    right: 0;
    top: 150px;
    font-size: 40px;
    font-weight: 400;
    letter-spacing: 2px;
  }
  .product-name {
    position: absolute;
    left: 0;
    right: 0;
    top: 368px;
    font-family: "Great Vibes", cursive;
    font-size: 72px;
    line-height: 1;
  }
  .product-type {
    position: absolute;
    left: 0;
    right: 0;
    top: 462px;
    font-size: 25px;
    letter-spacing: 1.5px;
  }
  .volume {
    position: absolute;
    left: 0;
    right: 0;
    top: 740px;
    font-size: 26px;
    letter-spacing: 1px;
  }
</style>
</head>
<body>
  <main class="canvas">
    <section class="label">
      <div class="notes-rule"></div>
      <p class="scent-notes">WHITE TEA | ORANGE | PALO SANTO</p>
      <div class="label-body">
        <h1 class="brand-name">VELNORA</h1>
        <h2 class="product-name">True Path</h2>
        <p class="product-type">FRAGRANCE OIL</p>
        <p class="volume">200 ML</p>
      </div>
    </section>
  </main>
</body>
</html>
```